Verra needs a new design we have an updated logo and want a high qualitative high end feel

feel and aesthetic should be high qualitative like the packaging in a zuvi or the qualatative weight/feel of an zuvi design. modern, elegant bold.probably just the verra logo on the backone vesion could be blue background white letter ... open to ideas
Target Market(s)
legal, insurance , medical, finance rho 740
Industry/Entity Type
Information Technology
Font styles to use
Serif

```html
<!DOCTYPE html>
<html lang="en">
<head>
<meta charset="utf-8">
<title>Verra Business Card</title>
<link rel="stylesheet" href="https://fonts.googleapis.com/css2?family=Montserrat:wght@400;500;700&display=swap">
<style>
  :root {
    --navy: #1c2c45;
    --white: #ffffff;
    --ink: #1c2c45;
    --rule: #4a5566;
    --backdrop: #2a2c2e;
  }
  * { box-sizing: border-box; margin: 0; padding: 0; }
  html, body { width: 1200px; height: 738px; overflow: hidden; }
  body {
    background: var(--backdrop);
    font-family: "Montserrat", sans-serif;
    position: relative;
  }
  .card {
    position: absolute;
    top: 232px;
    width: 480px;
    height: 274px;
    overflow: hidden;
  }
  .card-front { left: 90px; background: var(--navy); }
  .card-back { left: 630px; background: var(--white); color: var(--ink); }

  .front-wordmark {
    position: absolute;
    left: 0; right: 0; top: 100px;
    display: flex; justify-content: center; align-items: center; gap: 12px;
    color: var(--white);
    font-size: 60px; font-weight: 500; letter-spacing: 1px; line-height: 1;
  }
  .mark-dot { width: 10px; height: 10px; border-radius: 50%; background: currentColor; }

  .back-wordmark {
    position: absolute; left: 26px; top: 44px;
    display: flex; align-items: center; gap: 8px;
    font-size: 36px; font-weight: 500; line-height: 1; color: var(--ink);
  }
  .back-wordmark .mark-dot { width: 7px; height: 7px; }

  .holder { position: absolute; right: 24px; top: 36px; text-align: right; }
  .holder-name { font-size: 17px; font-weight: 700; letter-spacing: 0.5px; }
  .holder-role {
    margin-top: 2px; padding-top: 2px;
    border-top: 1px solid var(--rule);
    width: 200px; margin-left: auto;
    font-size: 12px;
  }
  .divider {
    position: absolute; left: 26px; top: 104px; width: 260px;
    border-top: 1px solid var(--rule);
  }
  .contacts {
    position: absolute; left: 30px; top: 112px;
    list-style: none; font-size: 14px; line-height: 19px;
  }
  .contacts li { display: flex; align-items: center; gap: 7px; }
  .contacts svg { width: 9px; height: 9px; }
  .contacts strong { font-weight: 700; }
  .wave { position: absolute; inset: 0; }
  .address {
    position: absolute; right: 24px; top: 146px;
    color: var(--white); text-align: right;
    font-size: 13px; line-height: 18px; font-style: normal;
  }
</style>
</head>
<body>
  <section class="card card-front">
    <div class="front-wordmark"><span>verra</span><span class="mark-dot"></span></div>
  </section>

  <section class="card card-back">
    <svg class="wave" viewBox="0 0 480 274" aria-hidden="true">
      <path d="M0,200 C100,225 180,205 230,150 C290,95 400,92 480,88 L480,274 L0,274 Z" fill="var(--navy)"/>
      <path d="M0,250 C130,262 230,255 300,228 C370,205 430,205 480,200" fill="none" stroke="var(--white)" stroke-width="4"/>
    </svg>

    <div class="back-wordmark"><span>verra</span><span class="mark-dot"></span></div>

    <div class="holder">
      <div class="holder-name">DANIEL REYES</div>
      <div class="holder-role">Director</div>
    </div>

    <div class="divider"></div>

    <ul class="contacts">
      <li>
        <svg viewBox="0 0 10 10"><path d="M2,1 L4,1 L4.5,3 L3.3,3.8 C3.8,5 5,6.2 6.2,6.7 L7,5.5 L9,6 L9,8 C5,8.5 1.5,5 2,1 Z" fill="var(--ink)"/></svg>
        <span>804 555-0142</span>
      </li>
      <li>
        <svg viewBox="0 0 10 10"><rect x="0.7" y="2" width="8.6" height="6" fill="none" stroke="var(--ink)" stroke-width="1"/><path d="M0.7,2 L5,5.5 L9.3,2" fill="none" stroke="var(--ink)" stroke-width="1"/></svg>
        <span>help@verramsg.com</span>
      </li>
      <li>
        <svg viewBox="0 0 10 10"><circle cx="5" cy="5" r="4.2" fill="none" stroke="var(--ink)" stroke-width="1"/><path d="M0.8,5 H9.2 M5,0.8 C3,3 3,7 5,9.2 M5,0.8 C7,3 7,7 5,9.2" fill="none" stroke="var(--ink)" stroke-width="0.8"/></svg>
        <span>www.<strong>verramsg</strong>.com</span>
      </li>
    </ul>

    <address class="address">
      2210 W Linden St Suite 301<br>
      Ashford, VA 23100
    </address>
  </section>
</body>
</html>
```